依頼詳細
会社の封筒デザインを依頼します。封筒は「シンプル」だけど「先進的」なデザインを希望します。封筒は淡い水色です。発注先の印刷会社さんはグラデーションがあるとコスト高になりますので、グラデーションは入れないでください。また、黒1色で考えておりますので宜しくお願いします。
長3の封筒は横むきでお願いします。
記載項目
表面:会社名/〒住所/電話/Fax/URL
サイズ
希望イメージ
• +5 0 +5
• シンプル
複雑
• 単色
カラフル
• 暗い
明るい
• 日常
高級
• 遊び心
厳粛
• 未来的
伝統的
• 女性的
男性的
納品ファイル
• 高解像度JPG (.jpg)
• イラストレーター形式 (.ai)
補足説明
住所や氏名を記載する場合の下線を薄めか、点線で入れ、端に御中の文字を入れて下さい。
依頼公開後の追記内容
ロゴデータ追加致しました
ファイルの追加が出来ていませんでしたので、再度投稿しました。
【イメージの追記】
イメージですが、透き通ったような?スタイリッシュな?都会的な?繊細な?
簡単にいうと、かっこいい?ようなイメージでお願いできたらと思います。
言葉で伝えるって難しいですね。
表現力が無くてすみません。

申し訳ございませんが、締切日を延期させていただきました。
これまでご提案下さいました方には、ご了承の程宜しくお願い致します。
■ 選んだ理由

シンプルで、弊社のイメージしていたものを表現してくれたようなデザインでした。

■ 提案者全員のお礼・コメント

どれもこれも素敵なデザインばかりで選ぶのが大変でした。
皆様のデザインに感謝いたします。ありがとうございました。
今後も、機会がございましたら、宜しくお願い致します。

```html
<!DOCTYPE html>
<html lang="ja">
<head>
<meta charset="UTF-8">
<title>青野製作所 封筒</title>
<link rel="stylesheet" href="https://fonts.googleapis.com/css2?family=Noto+Sans+JP:wght@400;700&display=swap">
<style>
  :root {
    --paper: #ffffff;
    --edge: #d6d6d6;
    --rule: #cfcfcf;
    --ink: #222222;
    --ink-soft: #555555;
    --tint: #e6e6e6;
  }
  * { margin: 0; padding: 0; box-sizing: border-box; }
  html, body { width: 867px; height: 1200px; overflow: hidden; background: var(--paper); }
  body { font-family: "Noto Sans JP", sans-serif; color: var(--ink); }
  .envelope {
    position: relative;
    width: 867px;
    height: 1200px;
    background: var(--paper);
    border: 2px solid var(--edge);
  }
  .address-line {
    position: absolute;
    left: 130px;
    height: 0;
    border-top: 2px solid var(--rule);
  }
  .address-line--1 { top: 438px; width: 608px; }
  .address-line--2 { top: 543px; width: 608px; }
  .address-line--3 { top: 650px; width: 540px; }
  .honorific {
    position: absolute;
    left: 690px;
    top: 620px;
    font-size: 26px;
    font-weight: 700;
    letter-spacing: 2px;
  }
  .brand-motif {
    position: absolute;
    left: 60px;
    top: 720px;
    width: 360px;
    height: 360px;
  }
  .company-row {
    position: absolute;
    left: 42px;
    top: 1112px;
    right: 28px;
    display: flex;
    align-items: center;
    gap: 14px;
  }
  .company-name {
    font-size: 32px;
    font-weight: 700;
    letter-spacing: 2px;
    white-space: nowrap;
  }
  .company-rules {
    flex: 1;
    height: 12px;
    border-top: 2px solid var(--ink-soft);
    border-bottom: 2px solid var(--ink-soft);
  }
  .contact {
    position: absolute;
    left: 42px;
    top: 1162px;
    display: flex;
    gap: 22px;
    font-size: 13px;
    color: var(--ink-soft);
    white-space: nowrap;
  }
</style>
</head>
<body>
  <div class="envelope">
    <div class="address-line address-line--1"></div>
    <div class="address-line address-line--2"></div>
    <div class="address-line address-line--3"></div>
    <span class="honorific">御中</span>

    <svg class="brand-motif" viewBox="0 0 360 360" role="img" aria-label="会社シンボルの大きな装飾エリア">
      <circle cx="180" cy="180" r="170" fill="var(--tint)"/>
    </svg>

    <div class="company-row">
      <span class="company-name">青野製作所</span>
      <div class="company-rules"></div>
    </div>

    <div class="contact">
      <span>〒000-0000 ○○○○○○○○○○○○○○○○○○</span>
      <span>TEL000-000-0000</span>
      <span>FAX000-000-0000</span>
      <span>http://www0000000000000000</span>
    </div>
  </div>
</body>
</html>
```